Website/Logo redesign: FieldKinship.com

We need a web design for a sports social network.
We have already built the web-site but are unhappy with the current design.
We like colours that evoke outdoors, eg sky blue and grass green.
Please see how it currently looks:
http://www.fieldkinship.example/4b1a9c3e7d2f5a8b0c6e1f3a9d7b2c5e/
We are happy for everything to change, including logo, icons etc or for you to keep anything you think will work with your new design.
Reason: We have not yet found the design we are happy with so will be providing more feedback and extending the deadine.
We have increased the budget and also agreed to pay a second place award.
I will be giving existing and any new designs feedback daily.
Target Market(s)
Our target audience are mainly young sports players, but also older ones too.
Industry/Entity Type
Social
Look and feel

```html
<!DOCTYPE html>
<html lang="en">
<head>
<meta charset="utf-8">
<title>FieldKinship – Dashboard</title>
<link rel="stylesheet" href="https://fonts.googleapis.com/css2?family=Source+Sans+3:wght@400;600&display=swap">
<style>
:root{
  --green-top:#9dd13c;
  --green-hi:#a9f22f;
  --green-lo:#78c806;
  --orange:#f2661b;
  --orange-hi:#fb9e27;
  --orange-lo:#f57616;
  --ink:#2b2b2b;
  --muted:#555;
  --line:#d2d2d2;
  --panel:#f3f3f3;
  --panel-dark:#e3e3e3;
  --page:#ffffff;
  --tick:#6cc11a;
}
*{box-sizing:border-box;margin:0;padding:0}
html,body{width:1200px;height:1112px;overflow:hidden;background:var(--page)}
body{font-family:"Source Sans 3",sans-serif;color:var(--ink)}
.stage{position:absolute;left:0;top:0;width:1300px;height:1205px;transform:scale(.92308);transform-origin:0 0;background:var(--page)}
.abs{position:absolute}
.topbar{left:0;top:0;width:1300px;height:28px;background:linear-gradient(#a6d65a,var(--green-top))}
.signout{right:212px;top:5px;color:#fff;font-size:13px}
.header{left:0;top:28px;width:1300px;height:104px;background:linear-gradient(var(--green-hi),var(--green-lo))}
.brand{left:181px;top:56px;color:#fff;font-size:38px;font-weight:600;letter-spacing:1px;line-height:44px}
.nav{left:494px;top:64px;width:614px;height:31px;background:#fff;border-radius:3px;display:flex;box-shadow:0 1px 2px rgba(0,0,0,.2)}
.nav a{display:flex;align-items:center;justify-content:center;font-size:13px;color:#444;text-decoration:none;border-right:1px solid #ccc}
.nav a:last-child{border-right:0}
.content{left:166px;top:132px;width:968px;height:1073px;background:var(--panel)}
.box{background:var(--panel-dark);border:1px solid #d0d0d0;border-radius:2px;box-shadow:0 1px 2px rgba(0,0,0,.08)}
.photo{background:linear-gradient(135deg,#c9a47a,#6b8b4a)}
.photo.b{background:linear-gradient(135deg,#7b8fa8,#b08e73)}
.photo.c{background:linear-gradient(135deg,#8a3a24,#c7794f)}
.photo.d{background:linear-gradient(135deg,#e9cfa3,#b98d5f)}
.btn-light{background:#fff;border:1px solid #c8c8c8;border-radius:3px;font-size:12px;color:#555;display:flex;align-items:center;justify-content:center}
.stat{background:#f6f6f6;border:1px solid #c8c8c8;border-radius:4px;text-align:center;font-size:13px;line-height:16px;padding-top:7px}
.stat b{display:block;color:var(--orange);font-weight:400;font-size:14px}
.bar{background:linear-gradient(var(--orange-hi),var(--orange-lo));color:#fff;font-size:18px;padding-left:15px;display:flex;align-items:center;border-radius:2px}
.team{background:#ececec;border:1px solid #d5d5d5;font-size:13px;padding-left:14px;display:flex;align-items:center}
.quote{background:#ececec;border:1px solid #d5d5d5;padding:10px 15px;font-size:14px;line-height:20px;color:#444;text-align:justify}
.quote .by{text-align:right;font-size:13px;color:#222;margin-top:2px}
.main{left:475px;top:148px;width:639px;height:1023px;background:var(--panel);border:1px solid #d3d3d3;box-shadow:0 1px 2px rgba(0,0,0,.1)}
.side{left:847px;top:157px;width:258px;height:576px;background:#f7f7f7;border:1px solid #d8d8d8}
.h{font-size:15px;color:#222}
.rule{height:1px;background:var(--line)}
.t14{font-size:14px}
.t13{font-size:13px}
.t12{font-size:12px;color:#333}
.or{color:var(--orange)}
.btn-or{background:linear-gradient(var(--orange-hi),var(--orange-lo));color:#fff;font-size:14px;display:flex;align-items:center;justify-content:center;border-radius:2px}
.comments{left:496px;top:318px;width:331px;height:321px;background:#fff;border:1px solid #d5d5d5;border-radius:3px}
.msg{font-size:13px;line-height:15px;color:#333;text-align:justify;width:231px}
.ago{font-size:13px;color:#333;text-align:right}
.input{background:#fff;border:1px solid #ccc;font-size:12px;color:#555;padding-left:8px;display:flex;align-items:center}
.table{left:861px;top:480px;width:233px;height:232px;background:#dedede;border:1px solid #cfcfcf}
.table-head{left:866px;top:485px;width:224px;height:30px;background:#fff;border:1px solid #d0d0d0;font-size:12px;color:var(--orange);padding-left:16px;display:flex;align-items:center}
.row{left:888px;width:180px;font-size:12px;display:flex}
.row span:first-child{width:132px}
.row span:nth-child(2){width:30px}
</style>
</head>
<body>
<div class="stage">
  <div class="abs topbar"></div>
  <div class="abs signout">Sign Out</div>
  <div class="abs header"></div>
  <div class="abs brand">FieldKinship</div>
  <nav class="abs nav">
    <a href="#" style="width:101px">Headlines</a>
    <a href="#" style="width:87px">My Stats</a>
    <a href="#" style="width:86px">Chllngrs</a>
    <a href="#" style="width:86px">Fixtures</a>
    <a href="#" style="width:79px">Teams</a>
    <a href="#" style="width:79px">Leagues</a>
    <a href="#" style="width:96px">Tools</a>
  </nav>

  <div class="abs content"></div>

  <!-- profile -->
  <div class="abs box" style="left:183px;top:149px;width:277px;height:157px"></div>
  <div class="abs photo" role="img" aria-label="Profile photo" style="left:197px;top:164px;width:53px;height:55px"></div>
  <div class="abs t13" style="left:265px;top:167px">Tom Reddings</div>
  <div class="abs btn-light" style="left:265px;top:192px;width:77px;height:23px">Edit Profile</div>
  <div class="abs rule" style="left:197px;top:230px;width:250px;background:#c9c9c9"></div>
  <div class="abs stat" style="left:199px;top:242px;width:50px;height:49px"><b>24</b>played</div>
  <div class="abs stat" style="left:267px;top:242px;width:51px;height:49px"><b>3</b>Teams</div>
  <div class="abs stat" style="left:335px;top:242px;width:50px;height:49px"><b>7</b>Awards</div>

  <div class="abs box" style="left:183px;top:319px;width:277px;height:52px"></div>
  <div class="abs" style="left:193px;top:329px;width:42px;height:31px;background:#d3d3d3;border-radius:2px">
    <svg width="42" height="31" viewBox="0 0 42 31"><path d="M21 8v15M13.5 15.5h15" stroke="#111" stroke-width="3.5"/></svg>
  </div>
  <div class="abs" style="left:248px;top:332px;font-size:18px">Create New Fixture</div>

  <div class="abs bar" style="left:184px;top:394px;width:274px;height:34px">All Teams</div>
  <div class="abs team" style="left:185px;top:440px;width:274px;height:31px">U15 Football Team B</div>
  <div class="abs team" style="left:185px;top:477px;width:274px;height:30px">Galatians House</div>
  <div class="abs team" style="left:185px;top:513px;width:274px;height:31px">U15 Rugby Team A</div>

  <div class="abs bar" style="left:184px;top:573px;width:274px;height:34px">Quote of the day</div>
  <div class="abs quote" style="left:185px;top:616px;width:274px;height:118px">Champions aren't made in the gyms. Champions are made from something they have deep inside them - a desire, a dream, a vision<div class="by">Marcus Ellery</div></div>

  <!-- main column -->
  <div class="abs main"></div>
  <div class="abs h" style="left:493px;top:166px">New Fixture</div>
  <div class="abs rule" style="left:493px;top:191px;width:332px"></div>
  <div class="abs t14" style="left:510px;top:216px">U15 Football Team vs <span class="or">Colossians House</span></div>
  <div class="abs t12" style="left:510px;top:237px">Sunday, 29th July, 1 PM</div>
  <div class="abs t14" style="left:512px;top:267px">RSVP</div>
  <div class="abs btn-or" style="left:554px;top:266px;width:89px;height:22px">Available</div>
  <div class="abs btn-or" style="left:654px;top:266px;width:88px;height:22px">Un Available</div>

  <div class="abs comments"></div>
  <div class="abs photo b" role="img" aria-label="Coach photo" style="left:518px;top:343px;width:40px;height:38px"></div>
  <div class="abs t13 or" style="left:575px;top:337px">Mr.Hartwell</div>
  <div class="abs msg" style="left:575px;top:364px">Don't be late minibus will be leaving at 11.30am on the dot, anybody late will miss</div>
  <div class="abs ago" style="left:640px;top:400px;width:162px">2 Miniutes ago</div>
  <div class="abs rule" style="left:513px;top:431px;width:293px"></div>
  <div class="abs photo c" role="img" aria-label="Player photo" style="left:523px;top:449px;width:40px;height:40px"></div>
  <div class="abs t13 or" style="left:575px;top:445px">Mr.Hartwell</div>
  <div class="abs msg" style="left:575px;top:472px">Don't be late minibus will be leaving at 11.30am on the dot, anybody late will miss</div>
  <div class="abs ago" style="left:640px;top:508px;width:162px">2 Miniutes ago</div>
  <div class="abs rule" style="left:513px;top:537px;width:293px"></div>
  <div class="abs photo d" role="img" aria-label="Player photo" style="left:526px;top:553px;width:36px;height:38px"></div>
  <div class="abs t13 or" style="left:575px;top:550px">Mr.Hartwell</div>
  <div class="abs msg" style="left:575px;top:577px">Don't be late minibus will be leaving at 11.30am on the dot, anybody late will miss</div>
  <div class="abs ago" style="left:640px;top:613px;width:162px">2 Miniutes ago</div>

  <div class="abs input" style="left:497px;top:648px;width:210px;height:27px">Leave Your Comment</div>
  <div class="abs btn-or" style="left:717px;top:649px;width:69px;height:25px;font-size:13px">Submit</div>

  <div class="abs h" style="left:493px;top:709px">Last Result</div>
  <div class="abs rule" style="left:493px;top:733px;width:332px"></div>
  <div class="abs t14" style="left:493px;top:750px">U15 Football Team vs <span class="or">Colossians House</span></div>
  <div class="abs t12" style="left:493px;top:771px">Sunday, 29th July, 1 PM</div>

  <div class="abs h" style="left:492px;top:814px">News Feed</div>
  <div class="abs rule" style="left:492px;top:838px;width:333px"></div>

  <div class="abs photo b" role="img" aria-label="Coach photo" style="left:493px;top:858px;width:40px;height:38px"></div>
  <div class="abs t13 or" style="left:550px;top:853px">Mr.Hartwell</div>
  <div class="abs msg" style="left:550px;top:880px">Don't be late minibus will be leaving at 11.30am on the dot, anybody late will miss</div>
  <div class="abs t12" style="left:549px;top:917px">RSP</div>
  <svg class="abs" style="left:576px;top:915px" width="48" height="21" viewBox="0 0 48 21"><circle cx="10.5" cy="10.5" r="10" fill="var(--tick)"/><path d="M6 11l3 3 6-7" stroke="#fff" stroke-width="2.4" fill="none"/><circle cx="35" cy="10.5" r="7" fill="#eee"/><path d="M32 7.5l6 6M38 7.5l-6 6" stroke="#999" stroke-width="2"/></svg>
  <div class="abs ago" style="left:640px;top:916px;width:137px">2 Miniutes ago</div>
  <div class="abs rule" style="left:488px;top:946px;width:293px"></div>

  <div class="abs photo c" role="img" aria-label="Player photo" style="left:498px;top:965px;width:40px;height:40px"></div>
  <div class="abs t13 or" style="left:550px;top:961px">Mr.Hartwell</div>
  <div class="abs msg" style="left:550px;top:988px">Don't be late minibus will be leaving at 11.30am on the dot, anybody late will miss</div>
  <div class="abs t12" style="left:549px;top:1026px">RSP</div>
  <svg class="abs" style="left:576px;top:1023px" width="48" height="21" viewBox="0 0 48 21"><circle cx="10.5" cy="10.5" r="10" fill="var(--tick)"/><path d="M6 11l3 3 6-7" stroke="#fff" stroke-width="2.4" fill="none"/><circle cx="35" cy="10.5" r="7" fill="#eee"/><path d="M32 7.5l6 6M38 7.5l-6 6" stroke="#999" stroke-width="2"/></svg>
  <div class="abs ago" style="left:640px;top:1025px;width:137px">2 Miniutes ago</div>
  <div class="abs rule" style="left:488px;top:1053px;width:293px"></div>

  <div class="abs photo d" role="img" aria-label="Player photo" style="left:501px;top:1069px;width:36px;height:38px"></div>
  <div class="abs t13 or" style="left:550px;top:1066px">Mr.Hartwell</div>
  <div class="abs msg" style="left:550px;top:1093px">Don't be late minibus will be leaving at 11.30am on the dot, anybody late will miss</div>
  <div class="abs t12" style="left:549px;top:1133px">RSP</div>
  <svg class="abs" style="left:576px;top:1130px" width="48" height="21" viewBox="0 0 48 21"><circle cx="10.5" cy="10.5" r="10" fill="var(--tick)"/><path d="M6 11l3 3 6-7" stroke="#fff" stroke-width="2.4" fill="none"/><circle cx="35" cy="10.5" r="7" fill="#eee"/><path d="M32 7.5l6 6M38 7.5l-6 6" stroke="#999" stroke-width="2"/></svg>
  <div class="abs ago" style="left:640px;top:1130px;width:137px">2 Miniutes ago</div>

  <!-- right column -->
  <div class="abs side"></div>
  <div class="abs h" style="left:860px;top:171px">Upcomming Fixtures</div>
  <div class="abs rule" style="left:860px;top:196px;width:234px"></div>
  <div class="abs t13" style="left:862px;top:211px">U15 Football Team vs</div>
  <div class="abs t13 or" style="left:862px;top:231px">Colossians House</div>
  <div class="abs t12" style="left:862px;top:255px">Sunday, 29th July, 1 PM</div>
  <div class="abs t13 or" style="left:862px;top:275px">Available</div>
  <div class="abs rule" style="left:860px;top:314px;width:234px"></div>
  <div class="abs t13" style="left:862px;top:334px">U15 Football Team vs</div>
  <div class="abs t13 or" style="left:862px;top:354px">Colossians House</div>
  <div class="abs t12" style="left:862px;top:378px">Sunday, 29th July, 1 PM</div>
  <div class="abs t13 or" style="left:862px;top:398px">Available</div>

  <div class="abs h" style="left:860px;top:440px">League Table</div>
  <div class="abs rule" style="left:860px;top:465px;width:234px"></div>
  <div class="abs table"></div>
  <div class="abs table-head">Ashbrook Inter House Football</div>
  <div class="abs row" style="top:533px"><span>Colossians</span><span>12</span><span>36</span></div>
  <div class="abs row" style="top:567px"><span>Phillippians</span><span>12</span><span>36</span></div>
  <div class="abs row" style="top:601px"><span>Galatians</span><span>12</span><span>36</span></div>
  <div class="abs row" style="top:635px"><span>Romans</span><span>12</span><span>36</span></div>
  <div class="abs row" style="top:669px"><span>Corinthians</span><span>12</span><span>36</span></div>
</div>
</body>
</html>
```